16 Page, A4. Company Brochure. Specialist Travel Company

Design of a 16 Page, A4 brochure for Travel Company specialising in Group Tours for Schools and Sports groups. The brochure should be broken into segments based on the companies subject and destination offerings. The design should inspire people to consider travelling.
Competitor Samples provided for structure and styling.
Text Content will be provided.
Images for use via the below link https://www.filvanta.com/sh/3kqpw8rzenx4m71/BBC2hLoq7TgWzrR9vNk4MeP3xb?dl=0
Target Market(s)
Schools
Industry/Entity Type
Travel
Look and feel

```html
<!DOCTYPE html>
<html lang="en">
<head>
<meta charset="utf-8">
<title>Wayfarer Group Travel – Brochure Spread</title>
<link href="https://fonts.googleapis.com/css2?family=Montserrat:wght@300;800&family=Open+Sans:ital,wght@0,400;0,600;1,400&display=swap" rel="stylesheet">
<style>
  :root{
    --backdrop:#2a2a2c;
    --paper:#f4f4f4;
    --red:#b3191f;
    --red-light:#cf4146;
    --ink:#3a3a3a;
    --white:#ffffff;
  }
  *{box-sizing:border-box;margin:0;padding:0}
  html,body{width:1200px;height:833px;overflow:hidden;background:var(--backdrop)}
  body{font-family:"Open Sans",Arial,sans-serif;position:relative}
  .spread{position:absolute;left:50px;top:28px;width:1100px;height:778px;display:flex;box-shadow:0 20px 50px rgba(0,0,0,.5)}
  .page{position:relative;width:550px;height:778px;background:var(--paper);overflow:hidden}
  .page-left{border-right:1px solid #d8d8d8}
  .band{position:absolute;inset:0;width:550px;height:778px}
  .photo{position:absolute;border:2px solid var(--white)}
  .section-title{position:absolute;font-family:"Montserrat",Arial,sans-serif;font-size:22px;font-weight:300;letter-spacing:.5px;color:var(--white)}
  .section-title strong{font-weight:800}
  .section-title::after{content:"";position:absolute;left:0;bottom:-8px;width:22px;height:3px;background:currentColor}
  .section-title.on-paper{color:var(--ink)}
  .section-title.on-paper strong{color:var(--red)}
  .section-title.on-paper::after{background:var(--red)}
  .copy{position:absolute;font-size:9.5px;line-height:1.45;color:var(--white)}
  .copy p{margin-bottom:7px}
  .copy.on-paper{color:var(--ink)}
  .ticks{list-style:none}
  .ticks li{position:relative;padding-left:13px;margin-bottom:1px}
  .ticks li::before{content:"";position:absolute;left:1px;top:3px;width:6px;height:3px;border-left:1.5px solid var(--white);border-bottom:1.5px solid var(--white);transform:rotate(-45deg)}
</style>
</head>
<body>
<div class="spread">

  <section class="page page-left">
    <svg class="band" viewBox="0 0 550 778" aria-hidden="true">
      <defs>
        <linearGradient id="redLeft" x1="0" y1="0" x2="1" y2="1">
          <stop offset="0" stop-color="#b3191f"/><stop offset=".6" stop-color="#cf4146"/><stop offset="1" stop-color="#b8242a"/>
        </linearGradient>
      </defs>
      <path d="M0,195 Q260,150 550,120 L550,600 Q280,565 0,555 Z" fill="url(#redLeft)"/>
    </svg>

    <div class="photo" role="img" aria-label="Floodlit ancient temple on a hill at dusk" style="left:85px;top:40px;width:265px;height:110px;background:linear-gradient(180deg,#1d3a78 0%,#35508a 45%,#c48a3c 70%,#5a4630 100%)"></div>
    <div class="photo" role="img" aria-label="Students seated in a large lecture hall" style="left:60px;top:150px;width:290px;height:85px;background:linear-gradient(135deg,#3b3a45,#7a6f73 50%,#d8d2cc)"></div>
    <div class="photo" role="img" aria-label="Empty classroom with desks and a blackboard" style="left:350px;top:60px;width:150px;height:230px;background:linear-gradient(160deg,#c9c4bb,#8d8a83 50%,#4f4a44)"></div>

    <h2 class="section-title" style="left:60px;top:255px">ABOUT <strong>US</strong></h2>

    <div class="copy" style="left:60px;top:300px;width:430px">
      <p>Wayfarer Group Travel is a division of Hoopline East. An Australian-owned and registered travel company, dedicated to providing enjoyable and educational journeys for schools, universities and individuals. As a full-service travel company, as well as your tour booking we can look after your international air travel, extension travel and travel insurance.</p>
      <p>Each Wayfarer tour is designed to provide a truly memorable experience for your school or club and participants will return with enhanced skills and knowledge gained from match experience, training and an educational sightseeing program. All of our tours share a number of common features:</p>
      <ul class="ticks">
        <li>The opportunity to play a series of matches with school and youth teams in the countries you visit</li>
        <li>Enjoy an educational syllabus-based itineraries sightseeing program linked to your school studies</li>
        <li>The opportunity to attend top-level matches in your chosen sport</li>
        <li>Skills development training sessions with international coaches</li>
        <li>A flexible cultural sightseeing program developed by experienced educators</li>
        <li>Visits to world-famous venues, museums and associated sports stores</li>
        <li>Relax and take it easy in different cities during your free time</li>
      </ul>
    </div>

    <div class="photo" role="img" aria-label="Basketball dropping through a hoop" style="left:60px;top:575px;width:140px;height:110px;background:linear-gradient(160deg,#9fb3c9,#d9c7b4 55%,#b4552a)"></div>
    <div class="photo" role="img" aria-label="Young footballer in red kit on a grass pitch" style="left:200px;top:580px;width:140px;height:115px;background:linear-gradient(180deg,#a9c3db,#d23a35 45%,#5f8a3a 75%,#3f6a2a)"></div>
    <div class="photo" role="img" aria-label="Baseball glove and wooden bats on grass" style="left:340px;top:590px;width:165px;height:125px;background:linear-gradient(150deg,#d6cbb8,#a37c55 50%,#6b5338)"></div>
  </section>

  <section class="page page-right">
    <svg class="band" viewBox="0 0 550 778" aria-hidden="true">
      <defs>
        <linearGradient id="redRight" x1="0" y1="0" x2="1" y2="1">
          <stop offset="0" stop-color="#b3191f"/><stop offset=".5" stop-color="#cf4146"/><stop offset="1" stop-color="#b3191f"/>
        </linearGradient>
      </defs>
      <path d="M0,35 L550,35 L550,520 Q290,440 0,430 Z" fill="url(#redRight)"/>
    </svg>

    <h2 class="section-title" style="left:50px;top:70px">WHY <strong>CHOOSE US</strong></h2>
    <div class="copy" style="left:50px;top:112px;width:450px">
      <p>Over the years, Wayfarer Group Travel has become recognised for the quality of its school and club tours with most of our schools/clubs being repeat clients. Several features of our operations make our sports and education tours stand out:</p>
    </div>

    <h2 class="section-title" style="left:50px;top:165px">OUR <strong>TEAM</strong></h2>
    <div class="copy" style="left:50px;top:207px;width:455px">
      <p>Our job is to make your tour as well-planned as possible. In Sydney and Melbourne, our expertise is broad ranging with product managers and administrative staff forming our sports and educational team.</p>
      <ul class="ticks">
        <li>Unique itineraries based on years of meeting the specific needs of school groups</li>
        <li>Direct management of your tour – we select the airlines, hotels, coaches, restaurants and tour guides</li>
        <li>We use experienced product managers who manage all logistical aspects of the tour</li>
        <li>A passionate, knowledgeable and dedicated admin team supporting each group</li>
        <li>Accommodation in selected two and three-star hotels and/or sports training facilities</li>
        <li>All-inclusive pricing, with air travel, insurance, match entry, most meals and tipping all included</li>
        <li>A team of local expert guides at cultural sites, selected over many years</li>
        <li>Fully documented risk management and hotel details to assist with official approval processes and all-inclusive pricing with no hidden extras</li>
      </ul>
    </div>

    <div class="photo" role="img" aria-label="Black and white photo of players on an outdoor court" style="left:50px;top:430px;width:165px;height:85px;background:linear-gradient(160deg,#d8d8d8,#8a8a8a 60%,#4a4a4a)"></div>
    <div class="photo" role="img" aria-label="Football resting on green grass" style="left:215px;top:445px;width:120px;height:90px;background:linear-gradient(170deg,#e9ece6,#b9c2b0 45%,#5f8d35)"></div>
    <div class="photo" role="img" aria-label="Students studying in a language classroom" style="left:45px;top:515px;width:120px;height:95px;background:linear-gradient(150deg,#cfcfcf,#6d6d6d 55%,#2f2f2f)"></div>
    <div class="photo" role="img" aria-label="Close-up of piano keys" style="left:165px;top:520px;width:105px;height:100px;background:linear-gradient(135deg,#efe6d6,#cbb894 50%,#3a2d22)"></div>
    <div class="photo" role="img" aria-label="Rows of ancient terracotta statues" style="left:270px;top:535px;width:110px;height:95px;background:linear-gradient(160deg,#b79a7e,#8b6d52 55%,#5d4a3a)"></div>
    <div class="photo" role="img" aria-label="Basketball team in a huddle on an indoor court" style="left:380px;top:490px;width:140px;height:200px;background:linear-gradient(180deg,#e6e6e6,#a8a8ac 35%,#3a3a44 70%,#b88a5a)"></div>

    <h2 class="section-title on-paper" style="left:50px;top:650px">GETTING <strong>STARTED</strong></h2>
    <div class="copy on-paper" style="left:50px;top:695px;width:320px">
      <p>You're ready to start planning your next tour! Here are the next steps... Please contact us by phone or email no later than 9-18 months before departure to discuss with us your tour, and we will work with you to tailor a suitable itinerary outline and provide an approximate costing. The exact tour price is confirmed 11 months before departure once flights become available.</p>
    </div>
  </section>

</div>
</body>
</html>
```